Quarlwick Builders Business Cards

I want to use the logo and make an unique business card that shows the textured Logo with brick and builings. I want to be able to stand out when I pass out business cards.

```html
<!DOCTYPE html>
<html lang="en">
<head>
<meta charset="utf-8">
<title>Quarlwick Builders Business Cards</title>
<link href="https://fonts.googleapis.com/css2?family=Oswald:wght@400;600;700&family=Lato:wght@400;700&display=swap" rel="stylesheet">
<style>
  :root{
    --stage:#2b2b2d;
    --concrete-light:#a9aba5;
    --concrete-mid:#8e908a;
    --concrete-dark:#6f716c;
    --brick:#c8462a;
    --brick-dark:#8a2e1c;
    --brick-light:#e0673f;
    --navy:#1d2a4a;
    --ink:#111111;
    --accent-red:#c9301c;
    --accent-orange:#f07a1a;
    --accent-green:#2fa336;
    --paper:#ffffff;
    --text-grey:#333333;
  }
  *{margin:0;padding:0;box-sizing:border-box}
  html,body{width:1200px;height:875px;overflow:hidden}
  body{background:var(--stage);position:relative;font-family:'Lato',sans-serif}
  .card{
    position:absolute;width:640px;height:366px;border-radius:18px;overflow:hidden;
    background:
      radial-gradient(circle at 30% 35%, rgba(255,255,255,.18), transparent 55%),
      radial-gradient(circle at 75% 70%, rgba(0,0,0,.12), transparent 50%),
      linear-gradient(135deg,var(--concrete-light),var(--concrete-mid) 55%,var(--concrete-dark));
    box-shadow:0 18px 40px rgba(0,0,0,.5);
  }
  .card--front{left:60px;top:50px}
  .card--back{left:500px;top:459px}
  .brand{position:absolute;display:flex;flex-direction:column;align-items:center}
  .brand__art{
    border-radius:10px;
    background:linear-gradient(180deg,#8c5a4a 0%,var(--brick-dark) 35%,var(--brick) 65%,var(--brick-light) 100%);
  }
  .brand__name{
    font-family:'Oswald',sans-serif;font-weight:700;color:var(--brick);
    text-transform:uppercase;letter-spacing:1px;white-space:nowrap;
  }
  .brand__services{
    font-family:'Oswald',sans-serif;font-weight:400;color:var(--navy);white-space:nowrap;
  }
  .card--front .brand{left:170px;top:58px;width:300px}
  .card--front .brand__art{width:230px;height:150px}
  .card--front .brand__name{font-size:34px;margin-top:8px}
  .card--front .brand__services{font-size:15px;margin-top:2px}
  .card--back .brand{left:40px;top:70px;width:250px}
  .card--back .brand__art{width:180px;height:118px}
  .card--back .brand__name{font-size:26px;margin-top:6px}
  .card--back .brand__services{font-size:12px;margin-top:2px}
  .swoosh{position:absolute;inset:0;width:100%;height:100%}
  .contact{position:absolute;right:34px;top:92px;text-align:right}
  .contact__name{font-family:'Oswald',sans-serif;font-weight:700;font-size:34px;color:var(--ink);letter-spacing:1px;line-height:1}
  .contact__title{font-family:'Lato',sans-serif;font-size:16px;color:var(--accent-red);margin:4px 0 16px}
  .contact__list{list-style:none}
  .contact__item{display:flex;justify-content:flex-end;align-items:center;gap:8px;font-size:14px;color:var(--text-grey);line-height:22px}
  .contact__item svg{width:12px;height:12px;fill:var(--accent-red)}
</style>
</head>
<body>

<section class="card card--front">
  <div class="brand">
    <div class="brand__art" role="img" aria-label="Textured brick wall with city buildings and mason tools"></div>
    <div class="brand__name">Quarlwick Builders</div>
    <div class="brand__services">Patios - Sidewalks - Retaining Walls - Foundations</div>
  </div>
</section>

<section class="card card--back">
  <div class="brand">
    <div class="brand__art" role="img" aria-label="Textured brick wall with city buildings and mason tools"></div>
    <div class="brand__name">Quarlwick Builders</div>
    <div class="brand__services">Patios - Sidewalks - Retaining Walls - Foundations</div>
  </div>
  <svg class="swoosh" viewBox="0 0 640 366" aria-hidden="true">
    <path d="M150 366 C250 340 360 300 400 190 C440 80 520 40 640 30 L640 366 Z" fill="var(--paper)"/>
    <path d="M180 332 C290 300 370 260 395 180 C425 80 500 35 610 22" fill="none" stroke="var(--accent-red)" stroke-width="5"/>
    <path d="M150 352 C260 330 330 300 355 250" fill="none" stroke="var(--accent-orange)" stroke-width="4"/>
    <path d="M430 120 C470 70 520 45 600 38" fill="none" stroke="var(--accent-green)" stroke-width="3"/>
  </svg>
  <div class="contact">
    <div class="contact__name">DORIAN HALE</div>
    <div class="contact__title">Founder &amp; CEO</div>
    <ul class="contact__list">
      <li class="contact__item">(555) 014-2290 <svg viewBox="0 0 12 12"><path d="M2 1l2 0 1 3-1.5 1a7 7 0 0 0 3.5 3.5L8 7l3 1 0 2c0 1-1 1-1 1C5 11 1 7 1 2c0 0 0-1 1-1z"/></svg></li>
      <li class="contact__item">(555) 014-2291 <svg viewBox="0 0 12 12"><rect x="3" y="0.5" width="6" height="11" rx="1"/></svg></li>
      <li class="contact__item">(555) 014-2292 <svg viewBox="0 0 12 12"><rect x="3" y="1" width="6" height="3"/><rect x="1" y="4.5" width="10" height="5" rx="1"/></svg></li>
      <li class="contact__item">info@quarlwickbuilders.com <svg viewBox="0 0 12 12"><rect x="0.5" y="2" width="11" height="8" rx="1"/></svg></li>
      <li class="contact__item">quarlwickbuilders.com <svg viewBox="0 0 12 12"><circle cx="6" cy="6" r="5.5"/></svg></li>
    </ul>
  </div>
</section>

</body>
</html>
```